Finance web application design

We need a design for a new responsive finance web application. It should look uber professional and modern.

Inspiration and design we like:

website:
http://www.brennickhale.com/

The application presented here:
http://markets.pelvantgrid.com/en/products/tools-applications/trading-investment-tools/zarvo-trading-software.html

https://apps.quillstore.example/us/app/ferncastle-for-tablet/id582917463?mt=8

The application presented here (Slatepad version):
https://apps.quillstore.example/en/app/trevik-forex-trading/id649205318?mt=8&utm_source=trevikButton

Target Market(s)

Private Investors

Industry/Entity Type

Finance

Number of Pages Required

5+ page

Font styles to use
Other font styles liked:
• Nobile

Requirements
Must have
• Colors for "up" changes: green
• Colors for "down" changes: red
• Fonts in tables must be very easy to read -
• Deliver design for all pages attached.
Nice to have
• A dark (gray) background
• Graphs should be shaded and partly transparent - orange or blue
• White text as "normal" - orange text / blue text for headers
Should not have
• White background

```html
<!DOCTYPE html>
<html lang="en">
<head>
<meta charset="utf-8">
<title>Ledgerwell.io – NRX Index</title>
<link href="https://fonts.googleapis.com/css2?family=Open+Sans:wght@400;600;700&family=Arimo:wght@400&display=swap" rel="stylesheet">
<style>
:root{
  --page:#1f282e;
  --topbar:#2a363c;
  --nav-active:#1d2529;
  --panel:#161d22;
  --panel-head:#2d3c43;
  --card:#0c1014;
  --card-border:#2a343b;
  --blue:#0a77b3;
  --blue-text:#1a7fb8;
  --orange:#f0913a;
  --white:#ffffff;
  --text:#e6e9eb;
  --muted:#9aa3a8;
  --table-head:#1b2130;
  --table-line:#262f36;
  --star-off:#2b343a;
}
*{box-sizing:border-box;margin:0;padding:0}
html,body{width:1200px;height:1085px;overflow:hidden}
body{background:var(--page);font-family:"Open Sans",sans-serif;color:var(--text);position:relative}
.abs{position:absolute}

/* top bar */
.topbar{left:0;top:0;width:1200px;height:80px;background:var(--topbar)}
.brand{left:24px;top:23px;display:flex;align-items:center;gap:8px;color:var(--orange);font-weight:700;font-size:25px;letter-spacing:-.5px}
.brand-mark{width:12px;height:12px;background:var(--orange)}
.nav{left:248px;top:0;height:80px;display:flex}
.nav a{display:block;height:80px;line-height:78px;padding:0 9px;color:var(--white);font-size:14px;font-weight:600;text-decoration:none}
.nav a.active{background:var(--nav-active);border-top:2px solid var(--orange);line-height:76px}
.search{left:802px;top:20px;width:220px;height:39px;border:1px solid #3d4a51;border-radius:3px;background:var(--nav-active);padding:0 14px;display:flex;align-items:center;justify-content:space-between;color:#6e7a80;font-size:14px}
.user{left:1043px;top:27px;display:flex;align-items:center;gap:10px;font-size:14px;font-weight:600;color:var(--white)}
.avatar{width:25px;height:25px;border-radius:50%;background:linear-gradient(#c9ccce,#6f767a)}
.power{left:1157px;top:29px}

/* main panel */
.panel{left:25px;top:98px;width:1150px;height:924px;background:var(--panel);border-radius:2px}
.panel-head{left:25px;top:98px;width:1150px;height:78px;background:var(--panel-head);border-bottom:1px solid #3a4a52}
.title{left:53px;top:119px;display:flex;align-items:center;gap:12px}
.title h1{font-size:24px;font-weight:600;color:var(--white)}
.title .change{font-size:16px;font-weight:600;color:var(--orange);margin-left:2px}

.card{background:var(--card);border:1px solid var(--card-border)}
.card h2{font-size:20px;font-weight:600;color:var(--blue-text)}

/* chart */
.chart{left:49px;top:203px;width:582px;height:316px}
.range{left:49px;top:203px;width:582px;height:50px;background:var(--blue);display:flex;justify-content:flex-end}
.range span{height:50px;line-height:50px;padding:0 8px;font-size:16px;font-weight:600;color:var(--white);border-left:1px solid #0b5f8e}
.range span.on{background:var(--card);color:var(--blue-text)}
.plot{left:49px;top:253px}
.plot text{font-family:"Open Sans",sans-serif;font-size:12px;fill:#8c959a}

/* fund details */
.details{left:49px;top:549px;width:582px;height:450px;padding:23px 26px}
.details p{margin-top:18px;font-size:14px;line-height:25px;color:var(--text)}
.label{font-size:20px;font-weight:600;color:var(--blue-text)}
.small{font-size:14px;color:var(--text)}
.orange{color:var(--orange)}
.date{font-size:10px;color:var(--blue-text)}

/* indicators */
.indicators{left:661px;top:203px;width:491px;height:221px;padding:13px 22px 0 24px}
.indicator-row{display:flex;gap:21px}
.select{width:328px;height:57px;border:1px solid #3a454c;border-radius:2px;display:flex;justify-content:space-between;align-items:center;padding-left:18px;font-size:16px;font-weight:600;color:var(--text)}
.select i{width:53px;height:55px;background:var(--blue);display:flex;align-items:center;justify-content:center}
.num{width:94px;height:57px;border:1px solid #3a454c;border-radius:2px;padding-left:20px;line-height:55px;font-size:16px;font-weight:600}

.compare{left:661px;top:453px;width:491px;height:143px;padding:11px 22px 0 24px}
.compare .field{margin-top:21px;width:443px;height:57px;border:1px solid #3a454c;border-radius:2px;display:flex;align-items:center;justify-content:space-between;padding:0 14px 0 17px;font-size:16px;font-weight:600}

/* performance */
.performance{left:661px;top:626px;width:491px;height:373px;overflow:hidden}
.performance h2{padding:10px 0 0 21px;height:46px}
.perf-table{width:100%;border-collapse:collapse;table-layout:fixed;font-family:Arimo,sans-serif;font-size:14px}
.perf-table col.period{width:245px}
.perf-table th{height:40px;background:var(--table-head)}
.perf-table td{height:40.8px;text-align:center;border-top:1px solid var(--table-line);color:var(--text)}
.perf-table td+td,.perf-table th+th{border-left:1px solid var(--table-line)}
.perf-table td.up{color:var(--orange)}

.footer{left:0;top:1045px;width:1200px;text-align:center;font-size:14px;color:var(--white)}
</style>
</head>
<body>

<header class="abs topbar"></header>
<div class="abs brand"><span class="brand-mark"></span>Ledgerwell.io</div>
<nav class="abs nav">
  <a href="#">Dashboard</a><a href="#">Strategies</a><a href="#">Portfolios</a><a href="#" class="active">Market Data</a><a href="#">Cust Inst.</a><a href="#">User</a>
</nav>
<div class="abs search">Search for fund...
  <svg width="18" height="18" viewBox="0 0 18 18"><circle cx="7" cy="7" r="5.5" fill="none" stroke="#0a8fd6" stroke-width="2"/><line x1="11" y1="11" x2="16" y2="16" stroke="#0a8fd6" stroke-width="2.6" stroke-linecap="round"/></svg>
</div>
<div class="abs user"><div class="avatar" role="img" aria-label="User avatar"></div>John Doe</div>
<svg class="abs power" width="18" height="20" viewBox="0 0 18 20"><path d="M5 4.5A7 7 0 1 0 13 4.5" fill="none" stroke="#0a8fd6" stroke-width="2.2" stroke-linecap="round"/><line x1="9" y1="1.5" x2="9" y2="9" stroke="#0a8fd6" stroke-width="2.2" stroke-linecap="round"/></svg>

<main>
  <div class="abs panel"></div>
  <div class="abs panel-head"></div>
  <div class="abs title">
    <svg width="24" height="23" viewBox="0 0 24 23"><path d="M12 0l3.5 7.4 8.1 1-6 5.6 1.6 8L12 18l-7.2 4 1.6-8-6-5.6 8.1-1z" fill="var(--orange)"/></svg>
    <h1>NRX Index - 601,45</h1><span class="change">0,42 (+1,29%)</span>
  </div>

  <section class="abs card chart"></section>
  <div class="abs range"><span>1M</span><span>6M</span><span>YTD</span><span class="on">1Y</span><span>3Y</span><span>5Y</span><span>Max</span></div>
  <svg class="abs plot" width="581" height="265" viewBox="49 253 581 265">
    <g stroke="#1e262c" stroke-width="1">
      <line x1="124" y1="278" x2="610" y2="278" stroke-dasharray="4 4"/>
      <line x1="124" y1="318" x2="610" y2="318" stroke-dasharray="4 4"/>
      <line x1="124" y1="358" x2="610" y2="358" stroke-dasharray="4 4"/>
      <line x1="124" y1="398" x2="610" y2="398" stroke-dasharray="4 4"/>
      <line x1="124" y1="438" x2="610" y2="438" stroke-dasharray="4 4"/>
      <line x1="164" y1="270" x2="164" y2="478"/><line x1="203" y1="270" x2="203" y2="478"/><line x1="243" y1="270" x2="243" y2="478"/><line x1="283" y1="270" x2="283" y2="478"/><line x1="323" y1="270" x2="323" y2="478"/><line x1="363" y1="270" x2="363" y2="478"/><line x1="403" y1="270" x2="403" y2="478"/><line x1="443" y1="270" x2="443" y2="478"/><line x1="484" y1="270" x2="484" y2="478"/><line x1="523" y1="270" x2="523" y2="478"/><line x1="563" y1="270" x2="563" y2="478"/>
    </g>
    <line x1="124" y1="270" x2="124" y2="478" stroke="#3a444a"/>
    <line x1="124" y1="478" x2="610" y2="478" stroke="#3a444a"/>
    <polygon points="124,478 203,359 283,381 403,358 484,320 523,358 603,278 603,478" fill="#0a77b3" fill-opacity=".35"/>
    <polygon points="124,478 203,399 283,358 363,398 484,358 523,320 563,356 603,320 603,478" fill="#b36a2a" fill-opacity=".45"/>
    <polyline points="124,478 203,359 283,381 403,358 484,320 523,358 603,278" fill="none" stroke="#0a77b3" stroke-width="2"/>
    <polyline points="124,478 203,399 283,358 363,398 484,358 523,320 563,356 603,320" fill="none" stroke="#f0913a" stroke-width="2"/>
    <g fill="#0a77b3" stroke="#0c1014" stroke-width="2">
      <circle cx="203" cy="359" r="5"/><circle cx="283" cy="381" r="5"/><circle cx="403" cy="358" r="5"/><circle cx="484" cy="320" r="5"/><circle cx="523" cy="358" r="5"/><circle cx="603" cy="278" r="5"/>
    </g>
    <g fill="#f0913a" stroke="#0c1014" stroke-width="2">
      <circle cx="203" cy="399" r="5"/><circle cx="283" cy="358" r="5"/><circle cx="363" cy="398" r="5"/><circle cx="484" cy="358" r="5"/><circle cx="523" cy="320" r="5"/><circle cx="563" cy="356" r="5"/><circle cx="603" cy="320" r="5"/>
    </g>
    <g text-anchor="end">
      <text x="117" y="282">2500000</text><text x="117" y="322">2000000</text><text x="117" y="362">1500000</text><text x="117" y="402">1000000</text><text x="117" y="442">500000</text><text x="117" y="482">0</text>
    </g>
    <g text-anchor="middle">
      <text x="162" y="500">Jan</text><text x="203" y="500">Feb</text><text x="240" y="500">Mar</text><text x="283" y="500">Apr</text><text x="320" y="500">May</text><text x="362" y="500">Jun</text><text x="403" y="500">Jul</text><text x="443" y="500">Aug</text><text x="480" y="500">Sep</text><text x="522" y="500">Oct</text><text x="561" y="500">Nov</text><text x="598" y="500">Dec</text>
    </g>
  </svg>

  <section class="abs card details">
    <h2>Fund Details</h2>
    <p>Lorem ipsum dolor sit amet, consectetur adipiscing elit. Sed pretium, massa ut elementum viverra, arcu dui aliquet sapien, sed mollis nunc diam eget sapien. Vivamus sed luctus dolor. Ut quis diam bibendum, pretium tellus a, elementum magna.</p>
  </section>
  <div class="abs label" style="left:76px;top:749px">ISIN</div>
  <div class="abs small" style="left:77px;top:785px">NO0010095418</div>
  <div class="abs label" style="left:247px;top:749px">Rating</div>
  <svg class="abs" style="left:247px;top:785px" width="100" height="17" viewBox="0 0 100 17">
    <defs>
      <path id="rating-star" d="M8 0l2.35 5 5.45.65-4 3.75 1.05 5.4L8 12.1 3.15 14.8 4.2 9.4.2 5.65 5.65 5z"/>
    </defs>
    <use href="#rating-star" x="0" fill="var(--orange)"/>
    <use href="#rating-star" x="21.5" fill="var(--orange)"/>
    <use href="#rating-star" x="43" fill="var(--orange)"/>
    <use href="#rating-star" x="64.5" fill="var(--orange)"/>
    <use href="#rating-star" x="86" fill="var(--star-off)"/>
  </svg>
  <div class="abs label" style="left:76px;top:836px">Risk</div>
  <div class="abs small" style="left:76px;top:873px">Sharp</div>
  <div class="abs small" style="left:76px;top:903px">Avr Return</div>
  <div class="abs small" style="left:76px;top:933px">Std Dev</div>
  <div class="abs label" style="left:243px;top:836px">Cost</div>
  <div class="abs small" style="left:245px;top:876px">Marks Kjopsavg</div>
  <div class="abs small" style="left:426px;top:876px">---</div>
  <div class="abs small" style="left:245px;top:916px">Lopende Kostnader</div>
  <div class="abs date" style="left:245px;top:936px">21.01.2014</div>
  <div class="abs small orange" style="left:426px;top:916px">1,00%</div>
  <div class="abs small" style="left:245px;top:956px">Resultatbasert Avg.</div>
  <div class="abs small orange" style="left:426px;top:956px">10,00%</div>

  <section class="abs card indicators">
    <h2>Indicators</h2>
    <div class="indicator-row" style="margin-top:19px">
      <div class="select">Moving Average<i><svg width="22" height="13" viewBox="0 0 22 13"><path d="M2 2l9 9 9-9" fill="none" stroke="#fff" stroke-width="2.5"/></svg></i></div>
      <div class="num">50</div>
    </div>
    <div class="indicator-row" style="margin-top:21px">
      <div class="select">Moving Average<i><svg width="22" height="13" viewBox="0 0 22 13"><path d="M2 2l9 9 9-9" fill="none" stroke="#fff" stroke-width="2.5"/></svg></i></div>
      <div class="num">50</div>
    </div>
  </section>

  <section class="abs card compare">
    <h2>Compare</h2>
    <div class="field">Search for instruments by name....
      <svg width="24" height="24" viewBox="0 0 24 24"><circle cx="9.5" cy="9.5" r="7" fill="none" stroke="#0a8fd6" stroke-width="2.4"/><line x1="15" y1="15" x2="22" y2="22" stroke="#0a8fd6" stroke-width="3.2" stroke-linecap="round"/></svg>
    </div>
  </section>

  <section class="abs card performance">
    <h2>Performance</h2>
    <table class="perf-table">
      <colgroup><col class="period"><col></colgroup>
      <thead><tr><th></th><th></th></tr></thead>
      <tbody>
        <tr><td>1W</td><td class="up">+2,04%</td></tr>
        <tr><td>1M</td><td class="up">+1,04%</td></tr>
        <tr><td>3M</td><td class="up">+3,04%</td></tr>
        <tr><td>6M</td><td class="up">+6,04%</td></tr>
        <tr><td>YTD</td><td class="up">+10,04%</td></tr>
        <tr><td>1Y</td><td class="up">+23,04%</td></tr>
        <tr><td>3Y Ann</td><td class="up">+14,04%</td></tr>
      </tbody>
    </table>
  </section>
</main>

<footer class="abs footer">Copyright © 2014 Ledgerwell.io. All Rights Reserved</footer>
</body>
</html>
```